Semi-anonymous photo sharing and messaging app

Design app interface. App is needed for semi-anonymous communication.

For instance if you are on a tour bus, and you just met some people there. You want to send them pictures, but you don't want to give your plimora / email / phone number. So instead you use this app - current name is "eMilto" but you can also suggest a name if it fits really well with the theme of the design.

The initial version of the app is in the vonder store
https://shop.vanterix.net/store/apps/details?id=com.k7rwpzlm3qe9yhtab2xcu

the web version of this app is located here
https://bluekettlepath.net/

it is called Brisk Lantern Tide, because the password is four common words, and if you know those words, you can open the chat room.

As you can see app looks very poorly, and needs to be designed from bottom up. App should look nothing like it looks now. it should have original and easily recognizable feel to it.

I'm attaching screen-shots of the current app. Two screens - you enter password on one screen (or choose one of the existing "rooms") - you chat with peers on the second screen

It should be something neutral, so it's mainly for travellers, but could be used by anyone else. It should have vibe of comfort and security, but at the same time adventure and fun.

Please come back with more questions!

Target Market(s)

Travellers, mostly
single, groups,

Industry/Entity Type

Communication

Font styles to use
Sans Serif

Requirements
Must have
• original, light feel
• recognizable
• unique

```html
<!DOCTYPE html>
<html lang="en">
<head>
<meta charset="utf-8">
<title>eMilto – Enter Words</title>
<link rel="stylesheet" href="https://fonts.googleapis.com/css2?family=Noto+Sans:wght@400;500;700&display=swap">
<style>
  :root {
    --status-bar: #40b39e;
    --app-bar: #4cc3ad;
    --teal: #4cc4ae;
    --band: rgba(120, 135, 118, 0.55);
    --bg-deep: #3d6451;
    --bg-mid: #4d7566;
    --field: rgba(255, 255, 255, 0.13);
    --white: #ffffff;
    --olive: #9aa05a;
    --olive-icon: #b3ae5a;
  }
  * { box-sizing: border-box; margin: 0; padding: 0; }
  html, body { width: 675px; height: 1200px; overflow: hidden; }
  body {
    font-family: "Noto Sans", Arial, sans-serif;
    color: var(--white);
    position: relative;
    background: var(--bg-deep);
  }
  .backdrop {
    position: absolute; inset: 0;
    background:
      radial-gradient(ellipse 260px 340px at 20% 55%, rgba(120,130,80,0.45), transparent 70%),
      radial-gradient(ellipse 300px 260px at 45% 60%, rgba(50,95,70,0.8), transparent 70%),
      radial-gradient(ellipse 280px 340px at 95% 55%, rgba(95,130,125,0.6), transparent 70%),
      linear-gradient(180deg, #4a6f5e 0%, #3d6550 35%, #4a7262 70%, #4e7566 100%);
  }
  .status-bar {
    position: absolute; top: 0; left: 0; width: 675px; height: 47px;
    background: var(--status-bar);
  }
  .status-bar svg { position: absolute; }
  .status-time {
    position: absolute; right: 12px; top: 6px;
    font-size: 28px; font-weight: 400; letter-spacing: 0.5px;
  }
  .app-bar {
    position: absolute; top: 47px; left: 0; width: 675px; height: 94px;
    background: var(--app-bar);
  }
  .app-bar .back { position: absolute; left: 30px; top: 28px; }
  .app-title {
    position: absolute; left: 0; right: 0; top: 22px; text-align: center;
    font-size: 38px; font-weight: 500; letter-spacing: 1px; padding-right: 25px;
  }
  .prompt-band {
    position: absolute; top: 141px; left: 0; width: 675px; height: 53px;
    background: var(--band);
    text-align: center; font-size: 25px; line-height: 53px; letter-spacing: 0.6px;
  }
  .steps-line {
    position: absolute; left: 78px; top: 224px; width: 5px; height: 788px;
    background: var(--teal);
  }
  .step { position: absolute; left: 26px; width: 598px; height: 124px; }
  .step-hex { position: absolute; left: 0; top: 0; }
  .step-number {
    position: absolute; left: 0; top: 0; width: 110px; height: 124px;
    text-align: center; line-height: 124px; font-size: 38px; font-weight: 700;
  }
  .word-field {
    position: absolute; left: 142px; top: 30px; width: 456px; height: 63px;
    background: var(--field); border-radius: 3px;
    font-size: 26px; line-height: 63px; padding-left: 38px; letter-spacing: 0.5px;
  }
  .enter-button {
    position: absolute; left: 262px; top: 1013px; width: 151px; height: 58px;
    background: var(--olive); border-radius: 3px;
    text-align: center; line-height: 58px; font-size: 26px; letter-spacing: 1px;
  }
  .recent-label {
    position: absolute; left: 34px; top: 1088px; font-size: 26px; letter-spacing: 0.5px;
  }
  .recent-box {
    position: absolute; left: 22px; top: 1131px; width: 632px; height: 90px;
    border: 2px solid var(--white); border-radius: 6px;
  }
  .room-chip {
    position: absolute; left: 10px; top: 11px; width: 91px; height: 46px;
    border: 2px solid var(--teal); border-radius: 5px;
    text-align: center; line-height: 42px; font-size: 20px;
  }
  .clear-recent { position: absolute; right: 16px; top: 19px; }
</style>
</head>
<body>
  <div class="backdrop" role="img" aria-label="Soft blurred green travel scenery background"></div>

  <header class="status-bar">
    <svg width="22" height="20" viewBox="0 0 22 20" style="left:23px;top:13px" aria-hidden="true">
      <rect x="1" y="1" width="20" height="18" fill="none" stroke="#fff" stroke-width="2"/>
      <path d="M3 17 L9 10 L13 14 L16 11 L19 17 Z" fill="#fff"/>
    </svg>
    <svg width="34" height="26" viewBox="0 0 34 26" style="left:503px;top:10px" aria-hidden="true">
      <path d="M17 25 L0 7 A24 24 0 0 1 34 7 Z" fill="#fff"/>
    </svg>
    <svg width="26" height="26" viewBox="0 0 26 26" style="left:537px;top:10px" aria-hidden="true">
      <path d="M0 26 L26 0 L26 26 Z" fill="#fff"/>
    </svg>
    <svg width="18" height="30" viewBox="0 0 18 30" style="left:574px;top:8px" aria-hidden="true">
      <rect x="5" y="0" width="8" height="3" fill="#fff"/>
      <rect x="0" y="3" width="18" height="27" fill="#fff"/>
      <rect x="2" y="5" width="14" height="6" fill="#40b39e" opacity="0.5"/>
    </svg>
    <span class="status-time">4:20</span>
  </header>

  <nav class="app-bar">
    <svg class="back" width="26" height="40" viewBox="0 0 26 40" aria-label="Back">
      <path d="M22 3 L5 20 L22 37" fill="none" stroke="#fff" stroke-width="4.5" stroke-linecap="round"/>
    </svg>
    <h1 class="app-title">eMilto</h1>
  </nav>

  <div class="prompt-band">Enter Brisk Lantern Tide</div>

  <div class="steps-line"></div>

  <section class="steps">
    <div class="step" style="top:268px">
      <svg class="step-hex" width="110" height="124" viewBox="0 0 110 124"><polygon points="55,0 110,31 110,93 55,124 0,93 0,31" fill="var(--teal)"/></svg>
      <span class="step-number">1</span>
      <div class="word-field">Join</div>
    </div>
    <div class="step" style="top:462px">
      <svg class="step-hex" width="110" height="124" viewBox="0 0 110 124"><polygon points="55,0 110,31 110,93 55,124 0,93 0,31" fill="var(--teal)"/></svg>
      <span class="step-number">2</span>
      <div class="word-field">Group</div>
    </div>
    <div class="step" style="top:656px">
      <svg class="step-hex" width="110" height="124" viewBox="0 0 110 124"><polygon points="55,0 110,31 110,93 55,124 0,93 0,31" fill="var(--teal)"/></svg>
      <span class="step-number">3</span>
      <div class="word-field">My</div>
    </div>
    <div class="step" style="top:850px">
      <svg class="step-hex" width="110" height="124" viewBox="0 0 110 124"><polygon points="55,0 110,31 110,93 55,124 0,93 0,31" fill="var(--teal)"/></svg>
      <span class="step-number">4</span>
      <div class="word-field">Now</div>
    </div>
  </section>

  <div class="enter-button">ENTER</div>

  <div class="recent-label">RECENT :</div>
  <div class="recent-box">
    <div class="room-chip">Hello</div>
    <svg class="clear-recent" width="30" height="30" viewBox="0 0 30 30" aria-label="Clear">
      <circle cx="15" cy="15" r="13" fill="none" stroke="var(--olive-icon)" stroke-width="2"/>
      <path d="M10 10 L20 20 M20 10 L10 20" stroke="var(--olive-icon)" stroke-width="2.2" stroke-linecap="round"/>
    </svg>
  </div>
</body>
</html>
```